App Design

This is a 'video player' app - will be used to stream video files and watch them on a device. Need 3/4 skins for user customization.
Design will need to be versatile - used on: Kestrel4/4S/5 and vexTab2/3
Require an app design that shows the required functionality described by us, allows ease to navigate and visually creates a unique user experience.
App must have following pages: (refer to attached pages)
1. Search Page
2. Results Page
3. Video Page
4. End Page
3-4 skins for user preference
important: if you are interested please submit designs by tomorrow night - we will be picking from submitted designs - will make revisions and finalize the design within 4-5 days.
timing is crucial- please only submit if you can commit to timeline and design requirements. There will be refinements required.
Please see the attached update.
Additional reference files have been added to help in your efforts.
We have added a sample design that may help with your submissions. Please see brief
Target Market(s)
early adapters for technology / kestrel, tablet, zorbix users
Requirements
Should not have
- should not be generic design

```html
<!DOCTYPE html>
<html lang="en">
<head>
<meta charset="utf-8">
<title>Video Player Skin</title>
<link rel="stylesheet" href="https://fonts.googleapis.com/css2?family=Open+Sans:wght@400&display=swap">
<style>
  :root {
    --bg-edge: #32133d;
    --bg-core: #150a18;
    --accent: #cc00ff;
    --knob-dark: #2a2a2a;
    --knob-light: #4a4a4a;
    --gloss: rgba(255,255,255,0.28);
    --text: #ffffff;
  }
  html, body {
    margin: 0;
    padding: 0;
    width: 799px;
    height: 1200px;
    overflow: hidden;
    background: var(--bg-core);
  }
  .player {
    position: relative;
    width: 799px;
    height: 1200px;
    background: linear-gradient(to bottom, var(--bg-edge) 0%, var(--bg-core) 45%, var(--bg-edge) 100%);
  }
  .player-controls {
    position: absolute;
    inset: 0;
    width: 799px;
    height: 1200px;
  }
  .time-readout {
    font-family: "Open Sans", sans-serif;
    font-size: 31px;
    fill: var(--text);
    letter-spacing: 1px;
  }
  .accent { fill: var(--accent); }
  .track-empty { fill: none; stroke: var(--accent); stroke-width: 2; }
  .knob-ring { fill: url(#knobFill); stroke: var(--accent); stroke-width: 3; }
  .gloss { fill: var(--gloss); }
</style>
</head>
<body>
<main class="player">
  <svg class="player-controls" viewBox="0 0 640 961" preserveAspectRatio="none" aria-label="Video player controls">
    <defs>
      <linearGradient id="knobFill" x1="0" y1="0" x2="1" y2="0">
        <stop offset="0" stop-color="var(--knob-light)"/>
        <stop offset="0.5" stop-color="var(--knob-dark)"/>
        <stop offset="1" stop-color="var(--knob-light)"/>
      </linearGradient>
    </defs>

    <!-- progress slider -->
    <g class="progress-slider">
      <rect class="track-empty" x="45" y="54" width="20" height="150"/>
      <rect class="accent" x="44" y="200" width="22" height="393"/>
      <circle class="knob-ring" cx="58" cy="171" r="36"/>
      <rect class="accent" x="47" y="146" width="15" height="50"/>
      <circle class="gloss" cx="74" cy="171" r="20"/>
    </g>

    <text class="time-readout" transform="translate(44 610) rotate(90)">00:00</text>

    <!-- volume slider -->
    <g class="volume-slider">
      <rect class="track-empty" x="44" y="709" width="20" height="80"/>
      <rect class="accent" x="43" y="789" width="22" height="64"/>
      <circle class="knob-ring" cx="57" cy="790" r="32"/>
      <rect class="accent" x="48" y="768" width="13" height="44"/>
      <circle class="gloss" cx="71" cy="790" r="18"/>
      <path class="accent" d="M46 866 H64 L79 905 H31 Z"/>
    </g>

    <!-- transport buttons -->
    <g class="transport-buttons">
      <path class="accent" d="M110 320 L125 301 L140 320 Z"/>
      <rect class="accent" x="110" y="326" width="30" height="9"/>
      <path class="accent" d="M110 380 H140 L125 408 Z"/>
      <rect class="accent" x="110" y="449" width="30" height="12"/>
      <rect class="accent" x="110" y="468" width="30" height="12"/>
      <rect class="accent" x="110" y="517" width="30" height="8"/>
      <path class="accent" d="M110 532 H140 L125 550 Z"/>
    </g>

    <!-- main play button -->
    <g class="play-button">
      <circle cx="410" cy="460" r="96" fill="url(#knobFill)" stroke="var(--accent)" stroke-width="1.5"/>
      <path class="accent" d="M360 424 H461 L410 524 Z"/>
      <ellipse class="gloss" cx="460" cy="460" rx="41" ry="55"/>
    </g>
  </svg>
</main>
</body>
</html>
```